HomeBridle business card and stationary design

We are looking for a simple yet elegant design for our mortgage company business card and stationary.

The card should include:
Name (Derek Walsh)
Title (CEO)
Phone Number (614-208-3917)
Address (48 Birchfield Court, Suite 314, Marlow, OH 43952)
Email (email@homebridle-example.com)
"NMLS" i.e. (NMLS 61947)
"Company NMLS" (Company NMLS 472815)

See above

```html
<!DOCTYPE html>
<html lang="en">
<head>
<meta charset="UTF-8">
<title>HomeBridle Business Card</title>
<link href="https://fonts.googleapis.com/css2?family=Inter:wght@400;500;600;700&display=swap" rel="stylesheet">
<style>
  :root {
    --page-bg: #e9e6e1;
    --card-top: #f4f5f6;
    --card-dark: #16181b;
    --card-dark-edge: #0c0d0f;
    --brand-blue: #1c7fd4;
    --brand-ink: #1a1d21;
    --name-ink: #e6e7e9;
    --address-ink: #eceae6;
    --address-soft: #c6a6a1;
    --detail-ink: #d8ccb6;
    --rule: #8a7f74;
  }
  html, body {
    margin: 0;
    padding: 0;
    width: 1200px;
    height: 969px;
    overflow: hidden;
    background: var(--page-bg);
    font-family: "Inter", Arial, sans-serif;
  }
  .card {
    position: absolute;
    left: 165px;
    top: 238px;
    width: 870px;
    height: 492px;
    border-radius: 26px;
    overflow: hidden;
    background: var(--card-top);
    box-shadow: 0 14px 40px rgba(0,0,0,0.18);
  }
  .brand-name {
    position: absolute;
    left: 0;
    right: 0;
    top: 128px;
    text-align: center;
    font-size: 62px;
    font-weight: 600;
    letter-spacing: -0.5px;
    color: var(--brand-ink);
    line-height: 1;
  }
  .accent-rule {
    position: absolute;
    left: 0;
    right: 0;
    top: 272px;
    height: 6px;
    background: var(--brand-blue);
  }
  .contact-band {
    position: absolute;
    left: 0;
    right: 0;
    top: 282px;
    bottom: 0;
    background: linear-gradient(180deg, var(--card-dark) 0%, var(--card-dark-edge) 100%);
  }
  .identity {
    position: absolute;
    right: 481px;
    top: 36px;
    text-align: right;
  }
  .person-name {
    font-size: 30px;
    font-weight: 700;
    color: var(--name-ink);
    line-height: 1;
  }
  .person-title {
    margin-top: 6px;
    font-size: 19px;
    color: var(--brand-blue);
    line-height: 1;
  }
  .address {
    margin-top: 13px;
    font-size: 20px;
    line-height: 25px;
    color: var(--address-ink);
  }
  .address .soft { color: var(--address-soft); }
  .column-rule {
    position: absolute;
    left: 414px;
    top: 40px;
    width: 2px;
    height: 125px;
    background: var(--rule);
  }
  .details {
    position: absolute;
    left: 439px;
    top: 36px;
    color: var(--detail-ink);
    font-size: 20px;
    white-space: nowrap;
  }
  .licence { line-height: 25px; }
  .channels { margin-top: 8px; }
  .channel {
    display: flex;
    align-items: center;
    gap: 8px;
    line-height: 25px;
  }
  .channel svg { width: 16px; height: 16px; flex: none; }
</style>
</head>
<body>
  <div class="card">
    <div class="brand-name">HomeBridle</div>
    <div class="accent-rule"></div>
    <div class="contact-band">
      <div class="identity">
        <div class="person-name">Derek Walsh</div>
        <div class="person-title">CEO</div>
        <div class="address">
          48 Birchfield Court<br>
          Suite 314<br>
          <span class="soft">Marlow, OH 43952</span>
        </div>
      </div>
      <div class="column-rule"></div>
      <div class="details">
        <div class="licence">Company NMLS 472815</div>
        <div class="licence">NMLS&nbsp;&nbsp;61947</div>
        <div class="channels">
          <div class="channel">
            <svg viewBox="0 0 16 16" aria-hidden="true"><path fill="#1c7fd4" d="M3.6 1.2l2.3 2.6-1.2 1.9c.9 1.9 2.4 3.4 4.3 4.4l1.9-1.2 2.6 2.3-1.3 2.6C7 13.5 2.4 8.9 1.1 2.6z"/></svg>
            <span>614-208-3917</span>
          </div>
          <div class="channel">
            <svg viewBox="0 0 16 16" aria-hidden="true"><rect x="1.5" y="3.5" width="13" height="9" rx="1" fill="#1c7fd4"/><path d="M2 4.2l6 4.6 6-4.6" stroke="#16181b" stroke-width="1.3" fill="none"/></svg>
            <span>email@homebridle-example.com</span>
          </div>
          <div class="channel">
            <svg viewBox="0 0 16 16" aria-hidden="true"><circle cx="8" cy="8" r="6.5" fill="#1c7fd4"/><path d="M1.5 8h13M8 1.5c-2.2 2.2-2.2 10.8 0 13M8 1.5c2.2 2.2 2.2 10.8 0 13" stroke="#16181b" stroke-width="1" fill="none"/></svg>
            <span>homebridle.com</span>
          </div>
        </div>
      </div>
    </div>
  </div>
</body>
</html>
```